Boutique custom software development company needs new business card

Our nearly 20 year old custom software development company would like to better include the fact that we are now providing Bitcoin services. These new services are B2B include education (how to acquire and securely hold Bitcoin) and integrating Bitcoin payments into existing ecommerce sites or other existing systems. Please keep the card clean and simple. Attached is our current design and some other files. velquor.example

Target Market(s)

businesses owners interested in long term relationship

Industry/Entity Type

Custom software development and Bitcoin

Contact Information for Business Card

Dale Furness, dale@velquor.example, velquor.example, (555) 274-VELQ

Font styles to use
Other font styles liked:
• monospace

Requirements
Must have
• double-sided
Nice to have
• clean and simple
Should not have
• physical address

```html
<!DOCTYPE html>
<html lang="en">
<head>
<meta charset="utf-8">
<title>Velquor Business Card</title>
<link rel="stylesheet" href="https://fonts.googleapis.com/css2?family=Lato:wght@400;700&family=Poppins:wght@400;700;800&display=swap">
<style>
  :root {
    --bg: #2a2b2d;
    --card-white: #ffffff;
    --card-black: #1b1c1e;
    --pattern-a: #232427;
    --pattern-b: #3a3b3e;
    --orange: #f0781e;
    --blue: #3a6fbe;
    --ink: #2e2e2e;
    --rule: #9a9a9a;
  }
  * { box-sizing: border-box; margin: 0; padding: 0; }
  html, body {
    width: 1200px; height: 1108px; overflow: hidden;
    background: var(--bg);
  }
  .canvas {
    position: relative; width: 1200px; height: 1108px;
  }
  .card {
    position: absolute; top: 204px; width: 400px; height: 700px;
    border-radius: 30px; overflow: hidden;
  }
  .card--front { left: 150px; background: var(--card-white); }
  .card--back { left: 650px; background: var(--card-black); }

  .brand {
    position: absolute; top: 140px; left: 20px; right: 20px; text-align: center;
  }
  .brand__name {
    font-family: "Poppins", sans-serif; font-weight: 800;
    font-size: 62px; letter-spacing: 1px; color: var(--blue); line-height: 1;
  }
  .brand__tagline {
    font-family: "Lato", sans-serif; font-size: 21px; color: var(--blue);
    margin-top: 12px; letter-spacing: -0.2px; line-height: 1.2;
  }
  .brand__services {
    font-family: "Lato", sans-serif; font-weight: 700; font-size: 17px;
    color: var(--orange); margin-top: 6px; line-height: 1.2;
  }

  .person {
    position: absolute; top: 430px; left: 0; right: 0; text-align: center;
    font-family: "Poppins", sans-serif; font-weight: 800; font-size: 30px;
    letter-spacing: 0.5px; line-height: 1.2;
  }
  .person__first { color: var(--orange); }
  .person__last { color: var(--blue); }

  .icon-row {
    position: absolute; top: 498px; left: 40px; right: 40px;
    display: flex; align-items: center; gap: 10px;
  }
  .icon-row__rule { flex: 1; height: 1px; background: var(--rule); }
  .icon-row__icons { display: flex; gap: 6px; }
  .icon { width: 36px; height: 36px; display: block; }

  .contact {
    position: absolute; top: 556px; left: 0; right: 0; text-align: center;
    font-family: "Poppins", sans-serif; font-size: 19px; color: var(--ink);
    line-height: 1.5;
  }
  .contact__web-name { color: var(--blue); }

  .back-pattern {
    position: absolute; inset: 0;
    background: linear-gradient(135deg, var(--pattern-b) 0%, var(--pattern-a) 45%, var(--card-black) 100%);
  }
  .back-mark {
    position: absolute; top: 448px; left: 0; right: 0; text-align: center;
    font-family: "Poppins", sans-serif; font-weight: 800; font-size: 52px;
    color: var(--orange); letter-spacing: 1px; line-height: 1.2;
  }
</style>
</head>
<body>
<main class="canvas">
  <section class="card card--front" aria-label="Card front">
    <div class="brand">
      <div class="brand__name">VELQUOR</div>
      <div class="brand__tagline">developer of custom applications</div>
      <div class="brand__services">Bitcoin payments &amp; education</div>
    </div>

    <h1 class="person">
      <span class="person__first">DALE</span> <span class="person__last">FURNESS</span>
    </h1>

    <div class="icon-row">
      <span class="icon-row__rule"></span>
      <span class="icon-row__icons">
        <svg class="icon" viewBox="0 0 36 36" aria-label="Phone">
          <rect width="36" height="36" rx="6" fill="#3a6fbe"/>
          <path d="M9 14c0-3 4-5 9-5s9 2 9 5v2h-5v-2c-1-1-7-1-8 0v2H9z" fill="#fff"/>
          <rect x="11" y="17" width="14" height="10" rx="2" fill="#fff"/>
          <circle cx="18" cy="22" r="2.5" fill="#3a6fbe"/>
        </svg>
        <svg class="icon" viewBox="0 0 36 36" aria-label="Email">
          <rect width="36" height="36" rx="6" fill="#3a6fbe"/>
          <rect x="8" y="11" width="20" height="14" fill="#fff"/>
          <path d="M8 11l10 8 10-8" fill="none" stroke="#3a6fbe" stroke-width="1.6"/>
        </svg>
        <svg class="icon" viewBox="0 0 36 36" aria-label="Website">
          <rect width="36" height="36" rx="6" fill="#3a6fbe"/>
          <circle cx="18" cy="18" r="9" fill="#fff"/>
          <ellipse cx="18" cy="18" rx="4" ry="9" fill="none" stroke="#3a6fbe" stroke-width="1.4"/>
          <path d="M9 18h18" stroke="#3a6fbe" stroke-width="1.4"/>
        </svg>
      </span>
      <span class="icon-row__rule"></span>
    </div>

    <div class="contact">
      <p>(555) 274-VELQ</p>
      <p>dale@velquor.example</p>
      <p>www.<span class="contact__web-name">velquor</span>.example</p>
    </div>
  </section>

  <section class="card card--back" aria-label="Card back">
    <div class="back-pattern" role="img" aria-label="Tonal repeating brand pattern in dark greys"></div>
    <div class="back-mark">VELQUOR</div>
  </section>
</main>
</body>
</html>
```